Bright Valley Goods - Product Page

Looking for a design for our product pages to showcase all of the following information in an aesthetically pleasing way. <br/><br/>• Product price per piece & price breaks<br/>• Set up cost <br/>• Additional color cost<br/>• Imprint side <br/>• Product Dimensions<br/><br/>Attached are photos showing ideas we have come up with to display the information. <br/><br/>The link below shows how our product pages is currently laid out. <br/><br/>Link to webpage: https://www.brightvalleygoods.example/non-woven-reusable-promo-totes.html<br/>

Number of Pages Required

1 page

Colors
33b8a4
33a6d7
3277b5
fece3e
f9a040
a3cd3a

Requirements
Must have
• • Product price per piece & price breaks
• • Set up cost
• • Additional color cost
• • Imprint side
• • Product Dimensions

```html
<!DOCTYPE html>
<html lang="en">
<head>
<meta charset="utf-8">
<title>Bright Valley Goods – Non-Woven Reusable Promo Totes</title>
<link href="https://fonts.googleapis.com/css2?family=Roboto:wght@400;500;700&display=swap" rel="stylesheet">
<style>
:root{
  --green:#5aaa2e; --green-text:#4a9a22; --navy:#0f4c75; --blue:#3277b5; --link:#2f74b8;
  --teal:#0f9464; --yellow:#fece3e; --orange:#ff5a0a; --light-green:#eefbdf; --light-blue:#eaf4fb;
  --gray:#f2f2f2; --text:#222; --muted:#555; --star:#f5b400;
}
*{box-sizing:border-box;margin:0;padding:0}
html,body{width:821px;height:1200px;overflow:hidden;background:#fff}
body{font-family:"Roboto",sans-serif;color:var(--text)}
.page{position:absolute;left:0;top:0;width:1280px;height:1871px;transform:scale(.6414);transform-origin:0 0}
.abs{position:absolute}
/* header */
.brand{left:18px;top:22px;display:flex;align-items:center;gap:10px;font-size:34px;font-weight:700;color:var(--green-text)}
.brand-dot{width:22px;height:22px;border-radius:50%;background:var(--orange)}
.rush{left:369px;top:19px;width:72px;height:72px;border-radius:50%;background:#f0401a;color:#fff;text-align:center;font-weight:700;font-size:15px;line-height:17px;padding-top:14px;box-shadow:0 2px 4px rgba(0,0,0,.3)}
.rush small{display:block;font-size:9px;color:var(--yellow)}
.call{left:540px;top:33px;width:180px;text-align:center;font-size:14px}
.call b{display:block;font-size:21px;color:var(--navy);font-weight:700}
.toplinks{right:32px;top:10px;display:flex;gap:20px;font-size:12px;color:#333}
.social{right:32px;top:35px;display:flex;gap:14px}
.social span{width:11px;height:11px;border-radius:50%;background:var(--navy)}
.cart{left:824px;top:60px;display:flex;align-items:center;gap:3px}
.cart em{font-style:normal;background:var(--green);color:#fff;font-size:10px;padding:1px 6px;border-radius:3px}
.search{left:881px;top:56px;width:368px;height:31px;border:1px solid #ccc;font-size:11px;color:#777;padding:9px 8px}
.search svg{position:absolute;right:6px;top:6px}
.nav{left:0;top:108px;width:1280px;height:44px;background:var(--green);display:flex;justify-content:center;gap:58px;align-items:center;color:#fff;font-size:12px;font-weight:700}
.crumb{left:0;top:152px;width:1280px;height:33px;background:var(--navy);color:#fff;font-size:12px;padding:10px 16px}
.crumb b{margin-left:8px}
.title{left:18px;top:194px;font-size:25px;color:var(--green-text)}
.rule{left:0;top:226px;width:1280px;height:1px;background:var(--green)}
/* gallery */
.hero{left:18px;top:241px;width:404px;height:349px;border:2px solid var(--blue);border-radius:8px;overflow:hidden}
.hero div{width:100%;height:100%;background:linear-gradient(100deg,#e22b2f 0 45%,#c9b48c 55%)}
.thumb{width:87px;height:87px;border:1px solid var(--blue);border-radius:6px;padding:10px 20px}
.thumb i{display:block;width:100%;height:100%;border-radius:2px}
/* sku row */
.skutab{left:421px;top:241px;width:150px;height:40px;background:var(--blue);color:#fff;font-size:25px;font-weight:500;padding:5px 12px;border-radius:0 8px 0 0}
.skutab span{color:var(--yellow)}
.skuinfo{left:580px;top:254px;font-size:16px;color:var(--link)}
.skuinfo span{color:var(--muted)}
.stars{color:var(--star);letter-spacing:2px}
.rate{left:950px;top:253px;font-size:16px;color:var(--link)}
/* price tables */
.price{width:193px;border:1px solid var(--navy);border-radius:6px;overflow:hidden}
.price h3{height:45px;color:#fff;font-size:22px;font-weight:500;text-align:center;line-height:45px}
.price .row{display:grid;grid-template-columns:1fr 1fr;height:46px;border-top:1px solid #888;background:var(--light-blue);font-size:17px;text-align:center;line-height:46px}
.price .row span+span{border-left:1px solid #888}
.price .head{color:var(--link);height:49px;line-height:49px}
.prod{width:351px;border:1px solid var(--blue);border-radius:6px;overflow:hidden}
.prod h3{height:46px;color:#fff;font-size:22px;font-weight:500;text-align:center;line-height:46px}
.prod .hl{background:var(--yellow);height:32px;text-align:center;font-size:17px;line-height:32px;font-weight:500}
.prod .row{display:grid;grid-template-columns:208px 1fr;height:30px;border-top:1px solid #bbb;font-size:17px;line-height:30px}
.prod .row span{padding-left:11px}
.prod .row span+span{border-left:1px solid #bbb;padding-left:13px}
.btn{height:49px;width:249px;border-radius:6px;color:#fff;font-size:23px;font-weight:500;text-align:center;line-height:49px}
/* reviews */
.reviews{left:18px;top:798px;width:403px;height:244px;background:var(--gray)}
.reviews header{height:51px;background:var(--blue);color:#fff;font-size:18px;font-weight:500;padding:14px 15px;display:flex;justify-content:space-between}
.reviews h4{font-weight:400;font-size:17px;margin:13px 15px 0}
.reviews p{font-size:15px;line-height:24px;color:#444;margin:9px 15px 0}
.reviews a{display:block;text-align:right;color:var(--link);font-size:16px;margin:9px 10px 0}
/* form */
.form{left:448px;top:797px;width:798px;height:245px;background:var(--blue);border-radius:8px}
.field{position:absolute;width:364px;height:52px;background:#fff;font-size:19px;color:#666;padding:14px 20px}
.form h5{position:absolute;top:155px;width:100%;text-align:center;color:#fff;font-size:19px;font-weight:500}
.submit{position:absolute;left:274px;top:187px;width:249px;height:48px;background:var(--yellow);border-radius:6px;text-align:center;line-height:48px;font-size:22px;font-weight:700}
/* recommended */
.rec{left:0;top:1074px;width:429px;height:727px;background:var(--gray)}
.rec h2{position:absolute;left:19px;top:10px;font-size:34px;font-weight:500;color:#111}
.card{position:absolute;width:191px;text-align:center}
.card .ph{height:200px;border:1px solid var(--blue);border-radius:6px;background:#fff;padding:18px}
.card .ph i{display:block;width:100%;height:100%;border-radius:4px}
.card b{display:block;color:var(--link);font-size:17px;font-weight:500;margin-top:9px}
.card p{color:var(--link);font-size:15px;line-height:25px;white-space:nowrap;margin-left:-10px;margin-right:-10px}
.card p span{color:var(--navy)}
.card small{font-size:14px;color:var(--link)}
/* details */
.tab{top:1075px;width:194px;height:48px;background:var(--green);color:#fff;font-size:20px;text-align:center;line-height:48px;border-radius:6px 6px 0 0}
.tab.on{background:var(--blue);height:58px}
.details{left:448px;top:1133px;width:798px;border:2px solid var(--blue);border-top:none}
.details h3{font-size:20px;font-weight:500;color:var(--green-text);padding:8px 10px;border-top:2px solid var(--blue);border-bottom:1px solid var(--blue)}
.details .row{display:grid;grid-template-columns:156px 1fr;border-top:1px solid var(--blue);font-size:17px;color:#333}
.details .row:first-of-type{border-top:none}
.details .row span{padding:11px 10px}
.details .row span+span{border-left:1px solid var(--blue);padding-left:15px;line-height:24px}
.details ul{list-style:none;padding:2px 0 12px}
.details li{line-height:30px;padding-left:30px;position:relative}
.details li::before{content:"";position:absolute;left:2px;top:13px;width:5px;height:5px;border-radius:50%;background:#333}
</style>
</head>
<body>
<div class="page">
  <!-- header -->
  <div class="abs brand"><span class="brand-dot"></span>Bright Valley Goods</div>
  <div class="abs rush">FREE<br>RUSH<small>Click Here</small></div>
  <div class="abs call">Call Us Toll Free:<b>1-800-555-0142</b></div>
  <nav class="abs toplinks"><span>Home</span><span>About Us</span><span>Contact Us</span><span>Blog</span></nav>
  <div class="abs social"><span></span><span></span><span></span><span></span><span></span></div>
  <div class="abs cart"><svg width="18" height="16" viewBox="0 0 18 16"><path d="M0 1h3l2 9h10l2-7H5" fill="none" stroke="#111" stroke-width="2"/><circle cx="7" cy="14" r="1.6" fill="#111"/><circle cx="14" cy="14" r="1.6" fill="#111"/></svg><em>0</em></div>
  <div class="abs search">SEARCH ENTIRE STORE HERE...<svg width="18" height="18" viewBox="0 0 18 18"><circle cx="7.5" cy="7.5" r="5.5" fill="none" stroke="#5aaa2e" stroke-width="2.5"/><path d="M11.5 11.5l5 5" stroke="#5aaa2e" stroke-width="2.5"/></svg></div>
  <nav class="abs nav"><span>REUSABLE BAGS ▾</span><span>SEED PAPER ▾</span><span>REUSABLE BOTTLES ▾</span><span>LANYARDS ▾</span><span>ECO PROMO ITEMS ▾</span></nav>
  <div class="abs crumb">Home &nbsp;»<b>Non-Woven Reusable Promo Totes</b></div>
  <h1 class="abs title" style="font-weight:400">Non-Woven Reusable Promo Totes</h1>
  <div class="abs rule"></div>

  <!-- gallery -->
  <div class="abs hero"><div role="img" aria-label="Photo of red and tan non-woven tote bags with printed logos"></div></div>
  <div class="abs thumb" style="left:18px;top:600px"><i role="img" aria-label="Black tote" style="background:#1a1a1a"></i></div>
  <div class="abs thumb" style="left:124px;top:600px"><i role="img" aria-label="Hunter green tote" style="background:#1f5135"></i></div>
  <div class="abs thumb" style="left:230px;top:600px"><i role="img" aria-label="Blue tote" style="background:#1a87c9"></i></div>
  <div class="abs thumb" style="left:334px;top:600px"><i role="img" aria-label="Navy tote" style="background:#2c2d8c"></i></div>
  <div class="abs thumb" style="left:18px;top:695px"><i role="img" aria-label="Red tote" style="background:#df3b3b"></i></div>
  <div class="abs thumb" style="left:124px;top:695px"><i role="img" aria-label="Tan tote" style="background:#c1ae8a"></i></div>
  <div class="abs thumb" style="left:230px;top:695px"><i role="img" aria-label="Teal tote" style="background:#15c0c0"></i></div>
  <div class="abs thumb" style="left:334px;top:695px"><i role="img" aria-label="Yellow tote" style="background:#f5e04a"></i></div>

  <!-- sku -->
  <div class="abs skutab">SKU : <span>PP2</span></div>
  <div class="abs skuinfo">Size: <span>13” W x 14”H x 7”D</span> &nbsp;| Thinkness: <span>100 GSM</span></div>
  <div class="abs rate"><span class="stars">★★★★★</span> 38 Review(s) | Add Review</div>

  <div class="abs price" style="left:448px;top:289px">
    <h3 style="background:var(--navy)">In Stock</h3>
    <div class="row head"><span>Qty</span><span>Price</span></div>
    <div class="row"><span>1</span><span>$0.69</span></div>
    <div class="row"><span>100+</span><span>$1.46</span></div>
    <div class="row"><span>250+</span><span>$1.35</span></div>
    <div class="row"><span>500+</span><span>$1.30</span></div>
    <div class="row"><span>1000+</span><span>$1.26</span></div>
    <div class="row"><span>2500+</span><span>$1.23</span></div>
    <div class="row"><span>5000+</span><span>$1.19</span></div>
  </div>
  <div class="abs price" style="left:672px;top:289px">
    <h3 style="background:var(--green)">Overseas</h3>
    <div class="row head"><span>Qty</span><span>Price</span></div>
    <div class="row"><span>1</span><span>$0.69</span></div>
    <div class="row"><span>1000+</span><span>$1.14</span></div>
    <div class="row"><span>3000+</span><span>$0.94</span></div>
    <div class="row"><span>5000+</span><span>$0.89</span></div>
    <div class="row"><span>10000+</span><span>$0.84</span></div>
    <div class="row"><span>25000+</span><span>$0.74</span></div>
    <div class="row"><span>50000+</span><span>$0.69</span></div>
  </div>

  <div class="abs prod" style="left:895px;top:289px;background:var(--light-blue)">
    <h3 style="background:var(--blue)">In Stock Production</h3>
    <div class="hl">Include 1 Imprint Color</div>
    <div class="row"><span>Imprint Size</span><span style="color:var(--link)">8” W x 8” H</span></div>
    <div class="row"><span>Additional Colors</span><span style="color:var(--link)">$0.45 each</span></div>
    <div class="row"><span>Full Color Imprint 300+</span><span style="color:var(--link)">$1.00 each</span></div>
    <div class="row"><span>Set Up Fee</span><span style="color:var(--link)">$45 per Color</span></div>
  </div>
  <div class="abs prod" style="left:895px;top:507px;background:var(--light-green);border-color:var(--teal)">
    <h3 style="background:var(--teal)">Overseas Production</h3>
    <div class="hl">FREE 1 Color, 2 Location Imprint</div>
    <div class="row"><span>Imprint Size</span><span style="color:var(--teal)">Unlimited</span></div>
    <div class="row"><span>Additional Colors</span><span style="color:var(--teal)">$0.05 each</span></div>
    <div class="row"><span>Full Color Imprint</span><span style="color:var(--teal)">Call</span></div>
    <div class="row"><span>Set Up Fee</span><span style="color:var(--teal)">$45 per Color</span></div>
  </div>

  <div class="abs btn" style="left:448px;top:730px;background:var(--green)">Request A Quote</div>
  <div class="abs btn" style="left:721px;top:730px;background:var(--orange)">Buy Now</div>
  <div class="abs btn" style="left:994px;top:730px;background:var(--orange)">Order Free Sample</div>

  <!-- reviews -->
  <section class="abs reviews">
    <header><span>Customer Reviews (38)</span><span>‹ &nbsp; ›</span></header>
    <h4>Review by <b>DANIEL R</b> &nbsp; <span class="stars">★★★★★</span></h4>
    <p>These bags were a big time hit at my annual convention. Our logo really stood out nicely on the center of these eco-friendly bags. The cost fit within our budget. Great company to work with.</p>
    <a>See all (38) Customer Reviews</a>
  </section>

  <!-- sample form -->
  <section class="abs form">
    <div class="field" style="left:24px;top:20px">Name</div>
    <div class="field" style="left:410px;top:20px">Email</div>
    <div class="field" style="left:24px;top:88px">Phone</div>
    <div class="field" style="left:410px;top:88px">--Quantity--<span style="position:absolute;right:18px;color:#222">▼</span></div>
    <h5>COMPLETE THIS FORM &amp; RECEIVE A FREE SAMPLE</h5>
    <div class="submit">SUBMIT</div>
  </section>

  <!-- recommended -->
  <section class="abs rec">
    <h2>Recommended Products</h2>
    <div class="card" style="left:18px;top:63px"><div class="ph"><i role="img" aria-label="Green and red printed tote bags" style="background:linear-gradient(100deg,#27c24a 50%,#e8462f 50%)"></i></div><b>SKU : PP9</b><p>Size: 16” W x 12”H x 6”D</p><p>As Low as: <span>$0.54</span></p><small><span class="stars">★★★★★</span> 23 Review(s)</small></div>
    <div class="card" style="left:228px;top:63px"><div class="ph"><i role="img" aria-label="Purple and tan printed tote bags" style="background:linear-gradient(100deg,#7a55b5 50%,#e3cfa6 50%)"></i></div><b>SKU : PP21A</b><p>Size: 13” W x 15”H x 10”D</p><p>As Low as: <span>$0.69</span></p><small><span class="stars">★★★★★</span> 22 Review(s)</small></div>
    <div class="card" style="left:18px;top:399px"><div class="ph"><i role="img" aria-label="Blue and red printed tote bags" style="background:linear-gradient(100deg,#1d6bb0 50%,#df2b2f 50%)"></i></div><b>SKU : PP3A</b><p>Size: 13” W x 15”H x 10”D</p><p>As Low as: <span>$0.74</span></p><small><span class="stars">★★★★★</span> 27 Review(s)</small></div>
    <div class="card" style="left:228px;top:399px"><div class="ph"><i role="img" aria-label="Green and tan wide tote bags" style="background:linear-gradient(100deg,#2ea34a 50%,#d6c39c 50%)"></i></div><b>SKU : PP5A</b><p>Size: 19.5” W x 13”H x 8”D</p><p>As Low as: <span>$0.75</span></p><small><span class="stars">★★★★★</span> 27 Review(s)</small></div>
  </section>

  <!-- detail tabs -->
  <div class="abs tab on" style="left:448px">Details</div>
  <div class="abs tab" style="left:648px">Reviews</div>
  <div class="abs tab" style="left:849px">Additional Info</div>
  <div class="abs tab" style="left:1050px">Shipping Estimator</div>
  <section class="abs details">
    <h3>Non-Woven Promotional Tote Bags Wholesale</h3>
    <div class="row"><span>Name</span><span>Non-Woven Reusable Promo Totes</span></div>
    <div class="row"><span>SKU</span><span>PP2</span></div>
    <div class="row"><span>Size</span><span>13" W x 14" H x 7" D</span></div>
    <div class="row"><span>Thickness</span><span>100 GSM</span></div>
    <div class="row"><span>Available Colors</span><span>Black, Hunter Green, Kelly Green, Lime Green, Maui Blue, Navy Blue, Purple, Red, Royal Blue, Tan, Teal &amp; Yellow</span></div>
    <div class="row"><span>Imprint Area</span><span>8" W x 8" H</span></div>
    <div class="row"><span>Key Features</span><span><ul>
      <li>Spacious Main Compartment, 1274 Cubic Inches</li>
      <li>22” Carry Straps</li>
      <li>Made from 100 GSM Non-Woven Polypropylene</li>
      <li>Eco-Friendly and 100% Recyclable</li>
      <li>Removable Hard Bottom Insert at the Base</li>
      <li>5 Day Standard Production / RUSH service available</li>
      <li>10 Day Production for Full Color Artwork</li>
      <li>8” Wide x 8” High Imprint Area</li>
      <li>Made From Recycled Content</li>
    </ul></span></div>
  </section>
</div>
</body>
</html>
```